Email Banner: Brightfold

Need an email banner for https://brightfold-hub.io/ much the same design for the attatched just using the logo and brand as the guidance.

Tagline should be "Essential Whitepapers for Business Professionals" or "Whitepapers featured from the most reputable companies in the industry"

It will be going on an email that looks like this:

https://mailvista-demo.co/emails/preview/fullscreen/a71b3d2e-9c4f-4e8a-b12d-f05e6a8c1b3d

So dont make it to thick and clunky.

Target Market(s)

IT Proffesioanls

Industry/Entity Type

Information Technology

Logo Text

Essential Whitepapers for Business Professionals

Logo styles of interest
Abstract Logo
Font styles to use
Sans Serif

Colors
0054AA
0677BA
7BADD7
CADEEF
E8F1F8

Requirements
Must have
• Logo and colour scheme from the weblink provided: https://brightfold-hub.io/

```html
<!DOCTYPE html>
<html lang="en">
<head>
<meta charset="UTF-8">
<title>Brightfold — Email Banner</title>
<link href="https://fonts.googleapis.com/css2?family=Montserrat:wght@400;700&display=swap" rel="stylesheet">
<style>
  :root {
    --brand-blue: #0054aa;
    --brand-mid: #0677ba;
    --brand-sky: #7badd7;
    --brand-mist: #cadeef;
    --brand-ice: #e8f1f8;
    --ink-navy: #06214a;
    --paper: #ffffff;
  }
  html, body {
    margin: 0;
    padding: 0;
    overflow: hidden;
    background: var(--paper);
  }
  .banner {
    position: relative;
    width: 1200px;
    height: 188px;
    background: var(--paper);
    overflow: hidden;
    font-family: "Montserrat", Arial, sans-serif;
  }
  .banner__shape {
    position: absolute;
    inset: 0;
    width: 1200px;
    height: 188px;
  }
  .brand {
    position: absolute;
    left: 54px;
    top: 56px;
    height: 76px;
    display: flex;
    align-items: center;
    gap: 24px;
  }
  .brand__dot {
    width: 74px;
    height: 74px;
    border-radius: 50%;
    background: var(--brand-mid);
    flex: none;
  }
  .brand__name {
    font-weight: 700;
    font-size: 56px;
    letter-spacing: 0.5px;
    color: var(--ink-navy);
    line-height: 1;
  }
  .tagline {
    position: absolute;
    left: 600px;
    top: 61px;
    margin: 0;
    font-weight: 400;
    font-size: 27px;
    line-height: 29px;
    letter-spacing: 0.9px;
    color: var(--paper);
  }
</style>
</head>
<body>
  <div class="banner">
    <svg class="banner__shape" viewBox="0 0 1200 188" aria-hidden="true">
      <path fill="var(--brand-blue)"
            d="M0,166 L475,166 C505,166 530,146 537,120 L552,66 C561,38 585,21.5 612,21.5 L1200,21.5 L1200,187.3 L0,187.3 Z"/>
    </svg>

    <div class="brand">
      <span class="brand__dot" aria-hidden="true"></span>
      <span class="brand__name">Brightfold</span>
    </div>

    <p class="tagline">Whitepapers featured from the most<br>reputable companies in the industry.</p>
  </div>
</body>
</html>
```